Tobias Wrenfeld and Co stationary design

Name of business:
Tobias Wrenfeld and Co

Can be written as:
Tobias Wrenfeld and Co
Tobias Wrenfeld & Co
tobias wrenfeld & co

If broken into letters:
TW&Co
tw&co

We are a Railway Safety Training Company
Our focus is on rail safety, Rail Management, Safety Management, Train Control Training, Accident Investigation.

.

Project Deadline Extended Reason: The original date was set to commence as soon as the logo contest finished. Sketch guild started the project as soon as it was paid. Added Thursday, May 12, 2016

Target Market(s)

Professionals, CEO's and Managing Directors

Industry/Entity Type

Management Consulting

Font styles to use
Sans Serif

Requirements
Must have
• Professional, Sharp, Creative and modern
• Please note that this is for stationary concept which must include
• - business card
• - letterhead
• - envelope
• - with compliments slip
• - document cover (like book or folder cover)
• - dividers for folders....
• These must all have a common theme or style
Nice to have
• Keep if fresh
Should not have
• Please don't sent just fonts.... Must be creative

```html
<!DOCTYPE html>
<html lang="en">
<head>
<meta charset="utf-8">
<title>Tobias Wrenfeld &amp; Co – Stationery Set</title>
<link href="https://fonts.googleapis.com/css2?family=Source+Sans+3:ital,wght@0,400;0,600;0,700;1,700&display=swap" rel="stylesheet">
<style>
  :root{
    --blue:#17498c;
    --orange:#f6a12b;
    --paper:#ffffff;
    --ink:#1d1d1d;
    --backdrop:#ababab;
    --font:"Source Sans 3", Arial, sans-serif;
  }
  *{box-sizing:border-box;margin:0;padding:0}
  html,body{width:1200px;height:1200px;overflow:hidden}
  body{background:var(--backdrop);font-family:var(--font);color:var(--ink);position:relative}
  .sheet{position:absolute;background:var(--paper);overflow:hidden;box-shadow:6px 8px 10px rgba(0,0,0,.35)}
  .band{position:absolute;left:0;right:0;bottom:0;height:var(--h,11px)}
  .band i{position:absolute;inset:0}
  .band .blue{background:var(--blue);clip-path:polygon(0 0,calc(var(--split) + 5px) 0,var(--split) 100%,0 100%)}
  .band .orange{background:var(--orange);clip-path:polygon(calc(var(--split) + 9px) 0,100% 0,100% 100%,calc(var(--split) + 4px) 100%)}
  .wordmark{position:absolute;display:flex;align-items:center;gap:6px;color:var(--blue);font-weight:700;white-space:nowrap}
  .wordmark .dot{border-radius:50%;background:var(--blue);flex:none}
  .person{position:absolute;color:var(--blue);font-weight:700}
  .person .role{display:block;color:var(--ink);font-weight:400}
  .contacts{position:absolute;list-style:none;line-height:1.3}
  .contacts li{display:flex;align-items:center;gap:6px;white-space:nowrap}
  .contacts svg{flex:none;fill:var(--blue)}
  .contacts .addr{color:var(--blue);margin-top:4px;display:block}
  .rule-v{position:absolute;width:1px;background:var(--blue)}
</style>
</head>
<body>

<!-- Business card: logo face -->
<section class="sheet card-front" style="left:52px;top:46px;width:268px;height:162px">
  <div class="wordmark" style="left:0;right:0;top:70px;justify-content:center;font-size:15px"><span class="dot" style="width:12px;height:12px"></span>Tobias Wrenfeld &amp; Co</div>
  <div class="band" style="--split:70%;--h:11px"><i class="blue"></i><i class="orange"></i></div>
</section>

<!-- Business card: contact face, wordmark right -->
<section class="sheet card-contact" style="left:345px;top:46px;width:268px;height:162px">
  <p class="person" style="left:16px;top:25px;font-size:10px">Marcus Hale<span class="role" style="font-size:8.5px">Director</span></p>
  <div style="position:absolute;left:52px;top:43px;width:118px;height:1px;background:var(--blue)"></div>
  <div class="wordmark" style="right:12px;top:40px;font-size:8.5px">Tobias Wrenfeld &amp; Co</div>
  <ul class="contacts" style="left:17px;top:72px;font-size:8px">
    <li><svg width="7" height="8" viewBox="0 0 7 8"><path d="M1 0h5v8H1zM2 1v5h3V1z"/></svg>+1 555 014 2871</li>
    <li><svg width="7" height="8" viewBox="0 0 7 8"><path d="M1 1l2-1 1 2-1 1q1 2 3 3l1-1 1 2-2 1Q1 6 1 1z"/></svg>+1 555 019 3360</li>
    <li style="margin-top:3px"><svg width="8" height="7" viewBox="0 0 8 7"><path d="M0 2h8v5H0zM0 2l4 3 4-3"/></svg>info@wrenfeldco.example.au</li>
    <li><svg width="8" height="8" viewBox="0 0 8 8"><circle cx="4" cy="4" r="4"/></svg>www.wrenfeldco.example.au</li>
    <li class="addr" style="font-size:8px">88 Harbour Lane, Suite 210<br>Northgate, City 40120</li>
  </ul>
  <div class="band" style="--split:69%;--h:11px"><i class="blue"></i><i class="orange"></i></div>
</section>

<!-- Business card: contact face, wordmark left -->
<section class="sheet card-contact-alt" style="left:52px;top:239px;width:268px;height:162px">
  <p class="person" style="left:16px;top:21px;font-size:9.5px">Marcus Hale<span class="role" style="font-size:8.5px">Director</span></p>
  <div class="wordmark" style="left:18px;top:130px;font-size:8.5px">Tobias Wrenfeld &amp; Co</div>
  <div class="rule-v" style="left:135px;top:74px;height:68px"></div>
  <ul class="contacts" style="left:146px;top:73px;font-size:8px">
    <li><svg width="7" height="8" viewBox="0 0 7 8"><path d="M1 0h5v8H1zM2 1v5h3V1z"/></svg>+61 555 014 2871</li>
    <li><svg width="7" height="8" viewBox="0 0 7 8"><path d="M1 1l2-1 1 2-1 1q1 2 3 3l1-1 1 2-2 1Q1 6 1 1z"/></svg>+61 555 019 3360</li>
    <li style="margin-top:3px"><svg width="8" height="7" viewBox="0 0 8 7"><path d="M0 2h8v5H0zM0 2l4 3 4-3"/></svg>info@wrenfeldco.example.au</li>
    <li><svg width="8" height="8" viewBox="0 0 8 8"><circle cx="4" cy="4" r="4"/></svg>www.wrenfeldco.example.au</li>
    <li class="addr">88 Harbour Lane, Suite 210<br>Northgate, NS 40120</li>
  </ul>
</section>

<!-- Business card: reverse -->
<section class="sheet card-back" style="left:345px;top:239px;width:268px;height:162px;background:var(--blue)">
  <div role="img" aria-label="Repeating tonal brand pattern" style="position:absolute;inset:0;background:linear-gradient(135deg,#1d5299,#17498c 60%,#1a4e94)"></div>
  <div class="wordmark" style="right:14px;top:112px;font-size:8px;color:#fff">Tobias Wrenfeld &amp; Co</div>
</section>

<!-- With compliments slip -->
<section class="sheet comp-slip" style="left:677px;top:46px;width:318px;height:160px">
  <p style="position:absolute;right:10px;top:8px;color:var(--blue);font-size:10px;font-weight:600">With Compliments</p>
  <div class="wordmark" style="left:10px;top:134px;font-size:5px">Tobias Wrenfeld &amp; Co</div>
  <div class="rule-v" style="left:58px;top:114px;height:28px;opacity:.6"></div>
  <ul class="contacts" style="left:63px;top:115px;font-size:4px;color:var(--blue);line-height:1.2">
    <li>+61 555 019 3360</li><li>info@wrenfeldco.example.au</li><li>www.wrenfeldco.example.au</li>
    <li>88 Harbour Lane, Suite 210</li><li>Northgate, NS 40120</li>
  </ul>
  <div class="band" style="--split:89%;--h:11px"><i class="blue"></i><i class="orange"></i></div>
</section>

<!-- Envelope: front -->
<section class="sheet envelope-front" style="left:677px;top:226px;width:394px;height:196px">
  <div class="wordmark" style="left:13px;top:41px;font-size:5px">Tobias Wrenfeld &amp; Co</div>
  <p style="position:absolute;left:13px;top:49px;font-size:4.5px;color:var(--blue);line-height:1.2">88 Harbour Lane, Suite 210<br>Northgate, City 40120</p>
  <div class="band" style="--split:89%;--h:16px"><i class="blue"></i><i class="orange"></i></div>
</section>

<!-- Envelope: back -->
<section class="sheet envelope-back" style="left:677px;top:443px;width:394px;height:196px">
  <svg width="394" height="60" viewBox="0 0 394 60" style="position:absolute;left:0;top:0">
    <path d="M0 0H394L372 50Q368 58 358 58H36Q26 58 22 50Z" fill="var(--blue)"/>
  </svg>
  <div class="wordmark" style="left:0;right:0;top:24px;justify-content:center;font-size:6px;color:#fff">Tobias Wrenfeld &amp; Co</div>
</section>

<!-- Letterhead -->
<section class="sheet letterhead" style="left:52px;top:484px;width:453px;height:641px">
  <div class="wordmark" style="left:45px;top:75px;font-size:10px"><span class="dot" style="width:9px;height:9px"></span>Tobias Wrenfeld &amp; Co</div>
  <div class="rule-v" style="left:323px;top:34px;height:72px"></div>
  <ul class="contacts" style="left:331px;top:36px;font-size:6px">
    <li><svg width="5" height="6" viewBox="0 0 7 8"><path d="M1 1l2-1 1 2-1 1q1 2 3 3l1-1 1 2-2 1Q1 6 1 1z"/></svg>+1 555 019 3360</li>
    <li style="margin-top:3px"><svg width="6" height="5" viewBox="0 0 8 7"><path d="M0 2h8v5H0z"/></svg>info@wrenfeldco.example.au</li>
    <li><svg width="5" height="5" viewBox="0 0 8 8"><circle cx="4" cy="4" r="4"/></svg>www.wrenfeldco.example.au</li>
    <li class="addr">88 Harbour Lane, Suite 210<br>Northgate, City 40120</li>
  </ul>
  <div class="band" style="--split:69%;--h:19px"><i class="blue"></i><i class="orange"></i></div>
</section>

<!-- Presentation folder: back panel -->
<section class="sheet folder-back" style="left:584px;top:680px;width:266px;height:460px">
  <div class="wordmark" style="left:8px;top:425px;font-size:4.5px">Tobias Wrenfeld &amp; Co</div>
  <ul class="contacts" style="left:62px;top:418px;font-size:4px;color:var(--blue);line-height:1.25">
    <li>+61 555 014 2871</li><li>+61 555 019 3360</li>
  </ul>
  <ul class="contacts" style="left:118px;top:418px;font-size:4px;color:var(--blue);line-height:1.25">
    <li>info@wrenfeldco.example.au</li><li>www.wrenfeldco.example.au</li>
  </ul>
  <ul class="contacts" style="left:196px;top:418px;font-size:4px;color:var(--blue);line-height:1.25">
    <li>88 Harbour Lane, Suite 210</li><li>Northgate, City 40120</li>
  </ul>
</section>

<!-- Presentation folder: front cover -->
<section class="sheet folder-front" style="left:850px;top:680px;width:276px;height:460px">
  <div class="wordmark" style="left:0;right:0;top:80px;justify-content:center;font-size:10px"><span class="dot" style="width:9px;height:9px"></span>Tobias Wrenfeld &amp; Co</div>
  <svg width="276" height="180" viewBox="0 0 276 180" style="position:absolute;left:0;top:112px">
    <path d="M0 0Q90 10 170 60L80 150L0 180Z" fill="#c9d3de"/>
    <path d="M80 150L170 60Q205 40 276 38V60L170 180Z" fill="#d8dde3"/>
    <path d="M170 60Q205 40 276 38V88Q250 60 215 78Z" fill="var(--orange)"/>
    <path d="M0 0Q90 10 170 60Q205 40 276 38M0 180L80 150L170 60M80 150L165 210L276 130" fill="none" stroke="var(--blue)" stroke-width="1"/>
  </svg>
  <div role="img" aria-label="Cover photographs of professionals at work" style="position:absolute;left:0;top:112px;width:276px;height:180px"></div>
  <h2 style="position:absolute;left:0;right:0;top:340px;text-align:center;color:var(--blue);font-weight:400;font-size:19px;line-height:1.2">YOUR MAIN<br>HEADLINE HERE</h2>
  <p style="position:absolute;left:24px;right:18px;top:398px;font-size:7.5px;line-height:1.3;color:#333">Lorem Ipsum is simply dummy text of the printing and typesetting industry. Lorem Ipsum has been the industry's standard dummy</p>
</section>

</body>
</html>
```